a residential cleaning service needs a website

We need a website for our faith based residential cleaning service, we are called MARGOT'S CLEANING SERVICE. We want a website that is clean looking both for mobile version and desktop. We want to convey cleanliness and trust to our clients. The color scheme should go in hand with the colors of the LOGO. We would like an about page, statement of faith page, services page and also a page for a booking module that our CRM has provided for us to being able to code and dress said module is important. The website not only needs to market to new customers and convey our service but also be easy to use for existing clients to schedule cleanings and services.
Industry/Entity Type
Cleaning Service
Coding
Coded - Design and coding required
Number of Pages Required
4 page
Requirements
Must have
- About page
Statement of Faith page
services page
booking and login page

```html
<!DOCTYPE html>
<html lang="en">
<head>
<meta charset="utf-8">
<title>Services – Margot's Cleaning Service</title>
<link rel="stylesheet" href="https://fonts.googleapis.com/css2?family=Cinzel:wght@400;500&family=Poppins:wght@400;500;600&display=swap">
<style>
  :root {
    --brand: #1f4296;
    --brand-dark: #19357d;
    --ink: #1b1b1b;
    --nav: #3a3a3a;
    --card-bg: #e7eff8;
    --swoosh-gray: #4d4f55;
    --footer: #13233f;
    --footer-line: #2c3c5a;
    --white: #ffffff;
    --muted: #c9d1de;
  }
  * { box-sizing: border-box; margin: 0; padding: 0; }
  html, body { width: 974px; height: 1200px; overflow: hidden; background: var(--white); }
  body { position: relative; font-family: 'Poppins', sans-serif; color: var(--ink); }

  .site-header { position: absolute; top: 0; left: 0; width: 974px; height: 71px; background: var(--white); z-index: 5; }
  .brand-badge {
    position: absolute; left: 191px; top: 0; width: 136px; height: 134px;
    background: var(--white); border-radius: 50%;
    display: flex; align-items: center; justify-content: center; gap: 5px;
    z-index: 6; padding-top: 14px;
  }
  .brand-badge .dot { width: 8px; height: 8px; border-radius: 50%; background: var(--brand); flex: none; }
  .brand-badge .name {
    font-family: 'Cinzel', serif; font-weight: 500; font-size: 11px; line-height: 1.25;
    color: var(--brand); text-align: center; width: 96px;
  }
  .main-nav { position: absolute; top: 31px; left: 371px; display: flex; font-size: 8px; font-weight: 600; letter-spacing: 0.1px; }
  .main-nav a { position: absolute; color: var(--nav); text-decoration: none; white-space: nowrap; }
  .main-nav a.active { color: var(--brand); }
  .login-btn {
    position: absolute; left: 712px; top: 25px; width: 71px; height: 24px; border-radius: 12px;
    background: var(--brand); color: var(--white); font-size: 8px; font-weight: 600;
    display: flex; align-items: center; justify-content: center; gap: 6px;
  }

  .hero { position: absolute; top: 0; left: 0; width: 974px; height: 340px; }
  .hero-title {
    position: absolute; top: 146px; width: 974px; text-align: center;
    font-family: 'Cinzel', serif; font-size: 36px; color: var(--white); letter-spacing: 1px;
  }
  .breadcrumb {
    position: absolute; top: 198px; width: 974px; text-align: center;
    font-size: 10px; font-weight: 500; color: var(--white);
  }
  .breadcrumb .sep { margin: 0 9px; }

  .services-heading {
    position: absolute; top: 402px; width: 974px; text-align: center;
    font-family: 'Cinzel', serif; font-size: 28px; color: var(--brand); letter-spacing: 0.5px;
  }
  .heading-rule { position: absolute; top: 439px; left: 469px; width: 36px; height: 2px; background: #555; }

  .service-card {
    position: absolute; top: 474px; width: 188px; height: 281px;
    background: var(--card-bg); border-bottom: 1px solid var(--brand); text-align: center;
  }
  .service-card .photo { height: 124px; }
  .service-card .badge {
    position: absolute; top: 99px; left: 69px; width: 50px; height: 50px; border-radius: 50%;
    background: var(--brand); box-shadow: 0 0 0 3px rgba(31,66,150,0.35);
    display: flex; align-items: center; justify-content: center;
  }
  .service-card h3 { margin-top: 41px; font-size: 11.5px; font-weight: 600; color: var(--ink); }
  .service-card p { margin: 8px 12px 0; font-size: 8.3px; line-height: 14.2px; color: #2a2a2a; }

  .site-footer { position: absolute; top: 839px; left: 0; width: 974px; height: 361px; background: var(--footer); color: var(--white); }
  .socials { position: absolute; top: 34px; left: 191px; display: flex; gap: 10px; }
  .socials span { width: 25px; height: 25px; border-radius: 50%; background: #26344f; }
  .subscribe {
    position: absolute; left: 502px; top: 29px; width: 282px; height: 38px; border-radius: 19px;
    background: var(--white); display: flex; align-items: center;
  }
  .subscribe .field { margin-left: 21px; display: flex; align-items: center; gap: 7px; font-size: 10px; color: #8a8f99; }
  .subscribe .btn {
    position: absolute; right: 5px; top: 4px; width: 99px; height: 30px; border-radius: 15px;
    background: var(--brand); color: var(--white); font-size: 10.5px; font-weight: 600;
    display: flex; align-items: center; justify-content: center;
  }
  .rule { position: absolute; left: 190px; width: 594px; height: 1px; background: var(--footer-line); }
  .footer-brand { position: absolute; left: 190px; top: 122px; width: 190px; text-align: center; }
  .footer-brand .mark { display: flex; align-items: center; justify-content: center; gap: 6px; height: 90px; }
  .footer-brand .mark .dot { width: 9px; height: 9px; border-radius: 50%; background: var(--white); }
  .footer-brand .mark .name { font-family: 'Cinzel', serif; font-size: 13px; line-height: 1.3; width: 120px; }
  .footer-brand p { margin-top: 23px; font-size: 8.5px; line-height: 14px; }
  .footer-col h4 { font-family: 'Cinzel', serif; font-weight: 400; font-size: 15px; letter-spacing: 0.5px; }
  .quick-links { position: absolute; left: 394px; top: 126px; }
  .quick-links ul { list-style: none; position: relative; margin-top: 14px; width: 220px; height: 110px; font-size: 8.5px; }
  .quick-links li { position: absolute; }
  .contact { position: absolute; left: 598px; top: 126px; }
  .contact ul { list-style: none; margin-top: 15px; font-size: 8.5px; }
  .contact li { display: flex; gap: 8px; align-items: flex-start; line-height: 12px; margin-bottom: 11px; }
  .copyright { position: absolute; top: 329px; width: 974px; text-align: center; font-size: 7.5px; color: var(--muted); }
</style>
</head>
<body>

<section class="hero">
  <svg width="974" height="340" viewBox="0 0 974 340">
    <defs>
      <linearGradient id="heroTone" x1="0" y1="0" x2="1" y2="1">
        <stop offset="0" stop-color="#5e7dbd"/>
        <stop offset="0.5" stop-color="#4d6db3"/>
        <stop offset="1" stop-color="#3c5ca6"/>
      </linearGradient>
    </defs>
    <path role="img" aria-label="Photo of cleaners mopping and wiping a floor, tinted blue" d="M0,71 H974 V213 C760,300 300,320 0,212 Z" fill="url(#heroTone)"/>
    <path d="M0,212 C300,320 650,330 889,288 C650,348 250,360 0,250 Z" fill="var(--swoosh-gray)"/>
    <path d="M90,245 C350,320 700,310 974,213 V255 C700,330 350,330 90,245 Z" fill="var(--brand)" stroke="#ffffff" stroke-width="3"/>
  </svg>
  <h1 class="hero-title">SERVICES</h1>
  <div class="breadcrumb">Home<span class="sep">›</span>Services</div>
</section>

<header class="site-header">
  <div class="brand-badge"><span class="dot"></span><span class="name">MARGOT'S CLEANING SERVICE</span></div>
  <nav class="main-nav">
    <a href="#" style="left:0">HOME</a>
    <a href="#" style="left:49px">ABOUT</a>
    <a href="#" style="left:102px">STATEMENT OF FAITH</a>
    <a href="#" class="active" style="left:212px">SERVICES</a>
    <a href="#" style="left:277px">BOOKING</a>
  </nav>
  <div class="login-btn">
    <svg width="11" height="11" viewBox="0 0 12 12" fill="none" stroke="#fff" stroke-width="1"><circle cx="6" cy="4" r="2.6"/><path d="M1.5,11.5 C2,8 10,8 10.5,11.5"/></svg>
    LOGIN
  </div>
</header>

<h2 class="services-heading">OUR SERVICES</h2>
<div class="heading-rule"></div>

<article class="service-card" style="left:190px">
  <div class="photo" role="img" aria-label="Photo of three cleaners with a cleaning cart" style="background:linear-gradient(135deg,#c9c3b8,#7d8fae 55%,#6b88b8)"></div>
  <div class="badge"><svg width="22" height="22" viewBox="0 0 24 24" fill="none" stroke="#fff" stroke-width="1.3"><path d="M9,5 H21 M15,5 V21 M5,11 H9 V21 H3 V14 Z M6,11 V8 H8"/></svg></div>
  <h3>Move in – Move out</h3>
  <p>We understand that moving is a daunt-ing process and we are delighted to offer services if that means less stress for you. From ceiling to floor, we will take care of it!</p>
</article>

<article class="service-card" style="left:393px">
  <div class="photo" role="img" aria-label="Photo of a woman in rubber gloves holding cleaning sprays" style="background:linear-gradient(135deg,#e8e6e2,#d9c8c8 50%,#b86aa8)"></div>
  <div class="badge"><svg width="22" height="22" viewBox="0 0 24 24" fill="none" stroke="#fff" stroke-width="1.3"><path d="M8,20 V9 A4,4 0 0 1 16,9 V20 M16,20 H21 V16 M4,20 H20"/><circle cx="6" cy="18" r="2"/></svg></div>
  <h3>One Time Cleaning</h3>
  <p>Planning a party, hosting the in-laws, or just too busy to clean this week? We've got you covered! We offer our detailed cleaning expertise to those who aren't looking for a regular service.</p>
</article>

<article class="service-card" style="left:596px">
  <div class="photo" role="img" aria-label="Photo of a woman wiping a window with a cloth" style="background:linear-gradient(135deg,#b9a08a,#d8e2e6 50%,#e8903a)"></div>
  <div class="badge"><svg width="22" height="22" viewBox="0 0 24 24" fill="none" stroke="#fff" stroke-width="1.3"><path d="M20,3 L12,11 M12,11 L5,14 L10,20 L13,13 Z M7,16 L10,14"/></svg></div>
  <h3>Routine Cleaning</h3>
  <p>We can design a cleaning plan for you. Once a month, bi- monthly, weekly, what-ever you need we are there to help! Each cleaning service will be thorough and leave you satisfied.</p>
</article>

<footer class="site-footer">
  <div class="socials"><span></span><span></span><span></span><span></span></div>
  <div class="subscribe">
    <div class="field">
      <svg width="12" height="12" viewBox="0 0 12 12" fill="none" stroke="#8a8f99" stroke-width="0.9"><rect x="1" y="1.5" width="10" height="7.5" rx="1"/><path d="M3,4 H9 M3,6 H7 M3,9 V11 L5,9"/></svg>
      Email
    </div>
    <div class="btn">Subscribe</div>
  </div>
  <div class="rule" style="top:93px"></div>

  <div class="footer-brand">
    <div class="mark"><span class="dot"></span><span class="name">MARGOT'S CLEANING SERVICE</span></div>
    <p>Margot's Cleaning Service is a faith based cleaning business founded in middle Tennessee over 19 years ago.</p>
  </div>

  <div class="footer-col quick-links">
    <h4>QUICK LINKS</h4>
    <ul>
      <li style="left:0;top:0">About</li>
      <li style="left:0;top:20px">Statement of Faith</li>
      <li style="left:0;top:40px">Services</li>
      <li style="left:0;top:60px">Booking</li>
      <li style="left:0;top:80px">Contact</li>
      <li style="left:106px;top:0">Conditions</li>
      <li style="left:106px;top:20px">Terms of Use</li>
      <li style="left:106px;top:40px">Privacy</li>
    </ul>
  </div>

  <div class="footer-col contact">
    <h4>LET'S TALK</h4>
    <ul>
      <li><svg width="8" height="10" viewBox="0 0 10 10" fill="#3d64c4"><path d="M2,0.5 L4,2.5 L3,4 C3.8,5.5 4.5,6.2 6,7 L7.5,6 L9.5,8 L8,9.5 C4,9 1,6 0.5,2 Z"/></svg>+00 123 456 789</li>
      <li><svg width="8" height="10" viewBox="0 0 10 10" fill="#3d64c4"><path d="M0.5,2 H9.5 V8.5 H0.5 Z"/><path d="M0.5,2 L5,5.5 L9.5,2" stroke="#13233f" stroke-width="0.8" fill="none"/></svg>hello@margotscleaningservice.com</li>
      <li><svg width="8" height="10" viewBox="0 0 10 10" fill="none" stroke="#3d64c4" stroke-width="1.1"><path d="M5,9.5 C2,6 1.5,5 1.5,3.8 A3.5,3.5 0 0 1 8.5,3.8 C8.5,5 8,6 5,9.5 Z"/><circle cx="5" cy="3.8" r="1.1"/></svg>PO Box 41270 Elm st. 312,<br>Nashville, Tennessee, Us.</li>
    </ul>
  </div>

  <div class="rule" style="top:306px"></div>
  <div class="copyright">Copyright © 2020 MARGOT'S CLEANING SERVICE. All Rights Reserved</div>
</footer>

</body>
</html>
```